Yoga class opening. Little schedule for JUNE JULY and AUGUST

Flyer to promote an opening yoga class. The color of the docx haven't to be respected.

We want something joyfull, professional, clean and serious.

About the logo we oppened a contest at the same time so at the moment there is no logo but the logo color will be simple.

The phone number will change so you can poste a random one for the design that i can change by myself.

i recieved many creation in both side BUT i want something in 1 side :)

Target Market(s)

Yoga student. all age

Industry/Entity Type

It Professional

Logo Text

Yoga fern

Font styles to use
Sans Serif

Requirements
Must have
• The text present on the docx
Nice to have
• Some symbols about yoga ( Namasté signs, mandala, ... )
Should not have
• Not too much details it has to be clear.

```html
<!DOCTYPE html>
<html lang="fr">
<head>
<meta charset="utf-8">
<title>Yoga fern – Planning de l'été</title>
<link href="https://fonts.googleapis.com/css2?family=Amatic+SC:wght@400;700&family=Arimo:wght@400;700&display=swap" rel="stylesheet">
<style>
  :root {
    --sky: #35a4d8;
    --white: #ffffff;
    --ink: #1d1d1b;
    --sun: #f28a3c;
    --sun-soft: #f7b987;
  }
  * { margin: 0; padding: 0; box-sizing: border-box; }
  html, body { width: 846px; height: 1200px; overflow: hidden; background: var(--white); }
  .flyer {
    position: relative;
    width: 846px;
    height: 1200px;
    overflow: hidden;
    background: var(--white);
    font-family: "Arimo", Arial, sans-serif;
  }
  .schedule-panel {
    position: absolute;
    left: 22px;
    top: 22px;
    width: 802px;
    height: 790px;
    background: var(--sky);
    border-radius: 36px;
  }
  .month-title {
    position: absolute;
    font-family: "Amatic SC", sans-serif;
    font-weight: 400;
    font-size: 42px;
    line-height: 1;
    color: var(--white);
    text-transform: uppercase;
  }
  .month-title.june { left: 78px; top: 62px; }
  .month-title.july { right: 80px; top: 290px; }
  .month-title.august { left: 76px; top: 522px; }
  .schedule {
    position: absolute;
    color: var(--white);
    font-size: 14.5px;
    line-height: 23.3px;
    list-style: none;
    white-space: nowrap;
  }
  .schedule .label { font-weight: 700; }
  .schedule .gap { height: 23.3px; }
  .schedule.june { left: 81px; top: 114px; }
  .schedule.july { right: 80px; top: 347px; text-align: right; }
  .schedule.august { left: 77px; top: 577px; }
  .footer {
    position: absolute;
    left: 0; right: 0;
    text-align: center;
    color: var(--ink);
  }
  .footer.start { top: 951px; font-size: 20px; }
  .footer.contact { top: 1000px; font-size: 17px; line-height: 23px; }
  .footer.wish {
    top: 1098px;
    font-family: "Amatic SC", sans-serif;
    font-size: 44px;
    line-height: 1;
    color: var(--sun);
    text-transform: uppercase;
  }
  .corner-pattern {
    position: absolute;
    width: 210px;
    height: 220px;
    background: var(--sun-soft);
  }
  .corner-pattern.left { left: 0; top: 980px; border-radius: 0 100% 0 0; }
  .corner-pattern.right { right: 0; top: 980px; border-radius: 100% 0 0 0; }
</style>
</head>
<body>
<main class="flyer">
  <div class="schedule-panel" role="img" aria-label="Grande forme décorative bleue peinte au pinceau, encadrée de traits"></div>

  <h2 class="month-title june">Juin</h2>
  <ul class="schedule june">
    <li class="label">Stage découverte du YOGA 10h00 85 €:</li>
    <li>Du lundi 6 au vendredi 10 juin : 10h00 à 12h00 ou 18h00 à 20h00</li>
    <li>Du lundi 13 au vendredi 17 juin : 10h00 à 12h00 ou 18h00 à 20h00</li>
    <li>Du lundi 20 au vendredi 24 juin : 10h00 à 12h00 ou 18h00 à 20h00</li>
    <li>Du lundi 27 au vendredi 1er juillet : 10h00 à 12h00 ou 18h00 à 20h00</li>
    <li class="gap"></li>
    <li class="label">Atelier gestion du stress yoga/sophrologie 2h00 28 €:</li>
    <li>Samedi 11 juin 10h30 à 12h30</li>
    <li>Samedi 11 juin 15h à 17h00</li>
    <li>Dimanche 12 juin 10h30 à 12h30</li>
    <li>Dimanche 12 juin 14h à 16h00</li>
  </ul>

  <h2 class="month-title july">Juillet</h2>
  <ul class="schedule july">
    <li class="label">Stage initiation à l’ASHTANGA 10h00 85 €:</li>
    <li>Du lundi 4 au vendredi 8 juillet : 10h00 à 12h00 ou 18h00 à 20h00</li>
    <li>Du lundi 11 au vendredi 15 juillet : 10h00 à 12h00 ou 18h00 à 20h00</li>
    <li>Du lundi 18 au vendredi 22 juillet : 10h00 à 12h00 ou 18h00 à 20h00</li>
    <li>Du lundi 25 au vendredi 29 juillet : 10h00 à 12h00 ou 18h00 à 20h00</li>
    <li class="gap"></li>
    <li class="label">Atelier gestion du stress yoga/sophrologie 2h00 28 €:</li>
    <li>Samedi 9 juillet 10h30 à 12h30</li>
    <li>Samedi 9 juillet 15h00 à 17h00</li>
    <li>Dimanche 10 juillet 10h30 à 12h30</li>
    <li>Dimanche 10 juillet 14h00 à 16h00</li>
  </ul>

  <h2 class="month-title august">Aout</h2>
  <ul class="schedule august">
    <li class="label">Stage découverte du YOGA 10h00 85 €:</li>
    <li>Du lundi 1er au vendredi 5 août : 10h00 à 12h00 ou 18h00 à 20h00</li>
    <li>Du lundi 8 au vendredi 12 août : 10h00 à 12h00 ou 18h00 à 20h00</li>
    <li>Du lundi 15 au vendredi 19 août : 10h00 à 12h00 ou 18h00 à 20h00</li>
    <li>Du lundi 22 au vendredi 26 août : 10h00 à 12h00 ou 18h00 à 20h00</li>
  </ul>

  <p class="footer start">Démarrage du planning annuel le 5 septembre 2016</p>
  <p class="footer contact">Plus d’info et inscription: (22) 5550-4817<br>Ou via notre page Circlepage: Yoga fern</p>
  <p class="footer wish">Un bel ete a tous!</p>

  <div class="corner-pattern left" role="img" aria-label="Motif décoratif orange de vagues en arcs concentriques"></div>
  <div class="corner-pattern right" role="img" aria-label="Motif décoratif orange de vagues en arcs concentriques"></div>
</main>
</body>
</html>
```